Solace Chiropractic & Acupuncture Business Cards

I need a business card design that feels elevated. I am open to any of the logo designs uploaded. We have two doctors so I'll need to be able to change out the names.

Information:
Marnie Toller D.C., Dipl. Ac. ASA
584 W 12th St, Ste 320
Ashbrook, NE 67419
solacegrove.net
620-555-0147
drmarnie@solacegrove.com
Updates

We have designs we like now, we are just trying to choose between top contenders. Thanks for your submissions!

Contact Information for Business Card

noted in description

Requirements
Must have
• ability to edit info if possible
Nice to have
• Please see our website solacegrove.net for our style and colors

```html
<!DOCTYPE html>
<html lang="en">
<head>
<meta charset="utf-8">
<title>Solace Chiropractic &amp; Acupuncture — Business Cards</title>
<link href="https://fonts.googleapis.com/css2?family=Cormorant+Garamond:wght@500;600&family=Montserrat:wght@400;500&display=swap" rel="stylesheet">
<style>
  :root {
    --backdrop: #2e2e30;
    --card: #ffffff;
    --navy: #2b3349;
    --ink: #24262b;
    --rule: #3a3f4d;
  }
  * { box-sizing: border-box; margin: 0; padding: 0; }
  html, body {
    width: 1200px; height: 875px; overflow: hidden;
    background: var(--backdrop);
  }
  .sheet {
    width: 1200px; height: 875px;
    display: flex; align-items: center; justify-content: center; gap: 48px;
  }
  .card {
    width: 532px; height: 304px;
    background: var(--card);
    border-radius: 20px;
    box-shadow: 0 18px 40px rgba(0,0,0,0.35);
    position: relative;
  }
  .brand {
    display: flex; flex-direction: column; align-items: center; gap: 12px;
    font-family: "Cormorant Garamond", serif;
    font-weight: 600;
    color: var(--navy);
    text-align: center;
    letter-spacing: 0.14em;
    text-transform: uppercase;
  }
  .brand-circle {
    border: 1.5px solid var(--navy);
    border-radius: 50%;
  }
  .card-front { display: flex; align-items: center; justify-content: center; }
  .card-front .brand { font-size: 17px; line-height: 1.35; }
  .card-front .brand-circle { width: 64px; height: 64px; }

  .card-back { display: flex; align-items: center; }
  .card-back .brand {
    width: 230px; font-size: 13px; line-height: 1.35;
  }
  .card-back .brand-circle { width: 48px; height: 48px; }
  .divider {
    width: 1px; height: 170px; background: var(--rule);
  }
  .details {
    padding-left: 22px;
    font-family: "Montserrat", sans-serif;
    color: var(--ink);
  }
  .doctor-name {
    font-family: "Cormorant Garamond", serif;
    font-weight: 500;
    font-size: 25px;
    letter-spacing: 0.04em;
    color: var(--navy);
    text-transform: uppercase;
    line-height: 1;
  }
  .credentials { font-size: 11px; font-weight: 500; margin-top: 4px; }
  .address { font-size: 13px; line-height: 1.3; margin-top: 16px; }
  .contact-list { list-style: none; margin-top: 14px; }
  .contact-list li {
    display: flex; align-items: center; gap: 9px;
    font-size: 13px; line-height: 1.75;
  }
  .contact-list svg { width: 12px; height: 12px; fill: var(--ink); flex: none; }
</style>
</head>
<body>
<main class="sheet">
  <section class="card card-front" aria-label="Card front">
    <div class="brand">
      <span class="brand-circle"></span>
      <span>Solace Chiropractic<br>&amp; Acupuncture</span>
    </div>
  </section>

  <section class="card card-back" aria-label="Card back">
    <div class="brand">
      <span class="brand-circle"></span>
      <span>Solace Chiropractic<br>&amp; Acupuncture</span>
    </div>
    <span class="divider"></span>
    <div class="details">
      <h1 class="doctor-name">Marnie Toller</h1>
      <p class="credentials">D.C., Dipl. Ac. ASA</p>
      <p class="address">584 W 12th St, Ste 320<br>Ashbrook, NE 67419</p>
      <ul class="contact-list">
        <li>
          <svg viewBox="0 0 24 24" aria-hidden="true"><path d="M6.6 10.8a15 15 0 0 0 6.6 6.6l2.2-2.2a1 1 0 0 1 1-.25 11.4 11.4 0 0 0 3.6.57 1 1 0 0 1 1 1V20a1 1 0 0 1-1 1A17 17 0 0 1 3 4a1 1 0 0 1 1-1h3.5a1 1 0 0 1 1 1c0 1.25.2 2.45.57 3.57a1 1 0 0 1-.25 1z"/></svg>
          620-555-0147
        </li>
        <li>
          <svg viewBox="0 0 24 24" aria-hidden="true"><path d="M2 5h20v14H2z M4 7v.5l8 5 8-5V7l-8 5z" fill-rule="evenodd"/></svg>
          drmarnie@solacegrove.com
        </li>
        <li>
          <svg viewBox="0 0 24 24" aria-hidden="true"><path d="M12 2a10 10 0 1 0 0 20 10 10 0 0 0 0-20zm0 2c.9 0 2.2 2 2.7 5H9.3C9.8 6 11.1 4 12 4zM9.1 11h5.8a14 14 0 0 1 0 2H9.1a14 14 0 0 1 0-2zM4.1 11h3a16 16 0 0 0 0 2h-3a8 8 0 0 1 0-2zm12.8 0h3a8 8 0 0 1 0 2h-3a16 16 0 0 0 0-2zM9.3 15h5.4c-.5 3-1.8 5-2.7 5s-2.2-2-2.7-5z"/></svg>
          www.solacegrove.net
        </li>
      </ul>
    </div>
  </section>
</main>
</body>
</html>
```